professional coaching community needs new look for website

We require a website design that attracts professionals. We run a large, global professional coaching community (e.g. executive, business, personal coaches NOT sports coaches). Our members are committed to their professional and personal development and they enjoy building relationships with other coaches across the world. We also champion the success of coaches and the coaching industry by providing business support resources to our members. We do not mind which colours you use, but whatever the combination, the combinations must be professional and refined. It would be good to have some of the familiarity of the old site colours, with some new, more professional element. We have a number of requirements for the homepage and members design, and this is attached.

Reason: I am extending the deadline for this design, in order to give feedback and see how current designs can be tweaked.

Target Market(s)

Here are some ideas for images, which gives and idea of the target market also:

Ideas for website images:

1. http://www.pixelvarno.com/stock-photo-48213077-business-success.php?st=4b2a918 (I like the people in this one – they seem very dynamic and a good mix of women and men)
2. http://www.pixelvarno.com/stock-photo-51729406-business-communications.php?st=4b2a918 (I like all of the speech bubbles in this one, that’s what the MentraLoop community does – pairs up in two’s or small groups and engages in professional talking)
3. http://www.pixelvarno.com/stock-photo-37086152-global-business-working.php?st=4b2a918 (I like the combination of the world and the people talking in different groups)
4. http://www.pixelvarno.com/stock-photo-44861039-global-business-people.php?st=e512604 (I like the world in this one – would be good to see combination of world and #1 dynamic people, which is the MentraLoop community)

Industry/Entity Type

Building

Requirements
Must have
• See attached uploaded files including homepage design, member dashboard design, and example profile (profiles need to be included him banner design). Note that any text must not be build into graphic. It needs to be able to be edited via html.

```html
<!DOCTYPE html>
<html lang="en">
<head>
<meta charset="utf-8">
<title>MentraLoop – Reciprocal peer coaching, mentoring and supervision</title>
<link href="https://fonts.googleapis.com/css2?family=Roboto:ital,wght@0,300;0,400;0,500;0,700;1,400&display=swap" rel="stylesheet">
<style>
  :root {
    --green: #7fc487;
    --green-dark: #5e9e63;
    --panel-green: #5c9f5f;
    --navy: #1f3f73;
    --navy-btn: #2c4f86;
    --text: #555;
    --text-light: #777;
    --rule: #dcdcdc;
    --orange: #f08a14;
    --band: #efefef;
    --footer: #3a3a3a;
    --white: #fff;
  }
  * { box-sizing: border-box; margin: 0; padding: 0; }
  html, body { width: 793px; height: 1200px; overflow: hidden; }
  body { position: relative; background: var(--white); font-family: "Roboto", Arial, sans-serif; color: var(--text); }
  .abs { position: absolute; }

  /* header */
  .site-header { left: 0; top: 0; width: 793px; height: 93px; background: linear-gradient(#86c98d, #79bf80); }
  .brand { left: 80px; top: 30px; }
  .brand-name { font-size: 21px; font-weight: 500; color: var(--white); letter-spacing: .3px; display: flex; align-items: center; gap: 6px; }
  .brand-mark { width: 10px; height: 10px; border-radius: 50%; background: var(--navy); }
  .brand-tag { font-size: 8.5px; font-style: italic; color: var(--navy); margin-top: 2px; margin-left: 14px; line-height: 10px; }
  .lang { left: 630px; top: 11px; width: 84px; height: 20px; background: var(--white); border-radius: 2px; font-size: 7.5px; color: #666; display: flex; align-items: center; padding-left: 6px; gap: 6px; }
  .lang-flag { width: 17px; height: 10px; background: #2a3f7a; }
  .lang-caret { margin-left: auto; margin-right: 7px; }
  .main-nav { left: 272px; top: 59px; display: flex; height: 22px; }
  .main-nav a { color: var(--white); font-size: 10px; text-decoration: none; line-height: 22px; padding: 0 8px; }
  .main-nav a.is-active { background: var(--navy-btn); }

  /* hero */
  .hero { left: 0; top: 93px; width: 793px; height: 101px; background: linear-gradient(#ffffff 15%, #ececec 60%, #d6d6d6); }
  .hero-title { width: 793px; top: 108px; text-align: center; font-size: 24.5px; color: var(--navy); font-weight: 400; }
  .btn { display: flex; align-items: center; justify-content: center; color: var(--white); border-radius: 3px; font-weight: 500; }
  .btn-green { left: 349px; top: 152px; width: 102px; height: 26px; background: linear-gradient(#82c989, #5ea565); font-size: 11.5px; border: 1px solid #559a5b; }

  /* slider */
  .slider { left: 80px; top: 207px; width: 468px; height: 217px; background: #e8e8e8; padding: 3px; }
  .slider-photo { width: 100%; height: 100%; background: linear-gradient(100deg, #d8dde2 0%, #eef0f1 40%, #5a5f66 80%, #2d3137 100%); }
  .slider-caption { left: 80px; top: 338px; width: 468px; text-align: center; color: var(--white); font-size: 21px; line-height: 23px; font-weight: 400; }
  .btn-orange { left: 263px; top: 390px; width: 102px; height: 25px; background: linear-gradient(#f9a02a, #e57a0b); font-size: 11px; }

  /* section headings */
  .section-title { font-size: 16.5px; color: var(--navy); font-weight: 400; }
  .title-rule { height: 3px; background: var(--rule); }

  .why-list { left: 80px; top: 468px; list-style: none; font-size: 9.2px; color: var(--text); }
  .why-list li { height: 18.5px; display: flex; align-items: center; gap: 7px; }
  .tick { width: 9px; height: 9px; flex: none; }

  .h-rule { height: 1px; background: var(--rule); }
  .v-rule { width: 1px; background: var(--rule); }

  .video { left: 80px; top: 617px; width: 223px; height: 166px; background: #e4e4e4; padding: 2px; }
  .video-photo { width: 100%; height: 100%; background: linear-gradient(180deg, #d9dadb 0%, #a9a9a6 55%, #6b5f58 100%); }
  .play { left: 172px; top: 682px; }

  .event { left: 326px; width: 212px; }
  .event-title { font-size: 10.5px; color: #4c9550; font-weight: 500; margin-bottom: 5px; }
  .event-text { font-size: 8.2px; line-height: 13.3px; color: var(--text); }
  .event-text em { color: var(--navy); }
  .view-all { left: 326px; top: 778px; font-size: 8px; color: var(--navy); font-weight: 500; letter-spacing: .3px; }

  /* sidebar */
  .panel { background: var(--panel-green); color: var(--white); }
  .panel-title { font-size: 11px; font-weight: 500; }
  .field { height: 19px; background: var(--white); border-radius: 2px; font-size: 7.3px; color: #888; padding-left: 6px; display: flex; align-items: center; }
  .check { width: 9px; height: 9px; background: var(--white); }
  .btn-navy { background: var(--navy-btn); font-size: 8.5px; border-radius: 2px; }
  .panel-link { font-size: 8.5px; }
  .perk-list { list-style: none; font-size: 8.7px; line-height: 12px; }
  .perk-list li { display: flex; gap: 8px; margin-bottom: 6px; }
  .perk-list .tick { margin-top: 2px; }

  .promo { left: 555px; top: 680px; width: 159px; height: 101px; background: linear-gradient(#4b86c4 0%, #9cc6e8 55%, #e3dcc8 80%, #d2c8ae 100%); }
  .promo-title { left: 563px; top: 684px; font-size: 14px; color: var(--white); }
  .promo-list { left: 566px; top: 703px; list-style: none; font-size: 5.8px; color: var(--white); line-height: 8.5px; }

  /* welcome */
  .welcome-copy { left: 80px; top: 850px; width: 405px; font-size: 8.8px; line-height: 13.5px; color: #444; }
  .welcome-copy p { margin-bottom: 7px; }

  .quote-box { left: 509px; top: 849px; width: 205px; height: 171px; background: var(--panel-green); }
  .quote-text { left: 519px; top: 862px; width: 188px; font-size: 8.3px; line-height: 13.2px; font-style: italic; color: var(--white); text-indent: 30px; }
  .quote-mark { font-size: 48px; color: #8fc493; font-family: Georgia, serif; line-height: 1; }
  .quote-name { right: 136px; top: 990px; font-size: 8.5px; font-weight: 700; color: var(--navy); text-align: right; }
  .quote-place { right: 136px; top: 1003px; font-size: 8px; font-style: italic; color: #e5f1e6; text-align: right; }
  .quote-photo { left: 663px; top: 972px; width: 38px; height: 38px; border: 2px solid var(--white); background: linear-gradient(#e8e2dc, #5a4a44); }

  /* supporters */
  .supporters { left: 0; top: 1028px; width: 793px; height: 100px; background: var(--band); }
  .supporter { top: 1067px; width: 119px; height: 46px; background: var(--white); border: 1px solid #e2e2e2; display: flex; align-items: center; justify-content: center; font-size: 15px; color: #666; }
  .arrow { top: 1039px; }

  /* footer */
  .site-footer { left: 0; top: 1128px; width: 793px; height: 72px; background: var(--footer); }
  .copyright { left: 80px; top: 1151px; font-size: 7.8px; color: #d8d8d8; line-height: 15px; }
  .copyright span { color: var(--green); }
  .connect { left: 595px; top: 1141px; font-size: 8.5px; color: #e8e8e8; }
  .social { top: 1159px; width: 20px; height: 19px; border-radius: 3px; }
</style>
</head>
<body>

<header class="site-header abs">
  <div class="brand abs">
    <div class="brand-name"><span class="brand-mark"></span>MentraLoop</div>
    <div class="brand-tag">Reciprocal peer coaching,<br>mentoring and supervision</div>
  </div>
  <div class="lang abs"><span class="lang-flag" role="img" aria-label="UK flag"></span>ENGLISH<span class="lang-caret">▾</span></div>
  <nav class="main-nav abs">
    <a class="is-active">HOME</a><a>COACHING</a><a>MENTORING</a><a>SUPERVISION</a><a>RESOURCES</a><a>JOIN US</a><a>CONTACT US</a>
  </nav>
</header>

<section class="hero abs" role="img" aria-label="Soft grey perspective floor background"></section>
<h1 class="hero-title abs">Join the most dynamic coaching community in the world</h1>
<div class="btn btn-green abs">QUICK SIGNUP</div>

<!-- slider -->
<div class="slider abs"><div class="slider-photo" role="img" aria-label="Business people at a presentation with a flow chart on a glass board"></div></div>
<div class="abs" style="left:83px;top:338px;width:462px;height:48px;background:rgba(30,30,30,.35)"></div>
<h2 class="slider-caption abs">Personal &amp; Professional Development<br>for Coaches</h2>
<div class="btn btn-orange abs">GET STARTED</div>

<!-- why choose -->
<h2 class="section-title abs" style="left:80px;top:433px">Why Choose MentraLoops?</h2>
<div class="title-rule abs" style="left:80px;top:459px;width:272px"></div>
<ul class="why-list abs">
  <li><svg class="tick" viewBox="0 0 10 10"><path d="M1 5l3 3 5-7" fill="none" stroke="#2c4f86" stroke-width="2"/></svg>Demonstrate integrity (coaching), competency (mentoring) and professionlism (supervision)</li>
  <li><svg class="tick" viewBox="0 0 10 10"><path d="M1 5l3 3 5-7" fill="none" stroke="#2c4f86" stroke-width="2"/></svg>Be part of one of the most active coaching communities in the world</li>
  <li><svg class="tick" viewBox="0 0 10 10"><path d="M1 5l3 3 5-7" fill="none" stroke="#2c4f86" stroke-width="2"/></svg>Be at your edge personally and professionally</li>
  <li><svg class="tick" viewBox="0 0 10 10"><path d="M1 5l3 3 5-7" fill="none" stroke="#2c4f86" stroke-width="2"/></svg>Remove the isolation normally attached to working for yourself</li>
  <li><svg class="tick" viewBox="0 0 10 10"><path d="M1 5l3 3 5-7" fill="none" stroke="#2c4f86" stroke-width="2"/></svg>All the known benefits of coaching, mentoring and supervision</li>
</ul>
<div class="h-rule abs" style="left:80px;top:570px;width:462px"></div>

<!-- video -->
<h2 class="section-title abs" style="left:80px;top:577px">Watch a Video</h2>
<div class="title-rule abs" style="left:80px;top:601px;width:222px"></div>
<div class="video abs"><div class="video-photo" role="img" aria-label="Presenter speaking to an audience at a whiteboard"></div></div>
<svg class="play abs" width="37" height="37" viewBox="0 0 37 37"><circle cx="18.5" cy="18.5" r="16.5" fill="rgba(0,0,0,.15)" stroke="#fff" stroke-width="2.5"/><path d="M14 10l12 8.5-12 8.5z" fill="#fff"/></svg>

<div class="v-rule abs" style="left:315px;top:581px;height:209px"></div>

<!-- events -->
<h2 class="section-title abs" style="left:326px;top:577px">Upcoming Events</h2>
<div class="title-rule abs" style="left:326px;top:601px;width:222px"></div>
<article class="event abs" style="top:615px">
  <h3 class="event-title">New rounds starting soon</h3>
  <p class="event-text">MentraLoop is an international community of coaches who engage in reciprocal coaching, mentoring and supervision for their own personal and professional development... <em>Read More</em></p>
</article>
<div class="h-rule abs" style="left:326px;top:690px;width:222px"></div>
<article class="event abs" style="top:695px">
  <h3 class="event-title">Lessons from the Field</h3>
  <p class="event-text">Most months, we pull together the collective professional learning of MentraLoops all around the world to deliver a short but power-packed issue of what we refer to as "Lessons from the Field...." <em>Read More</em></p>
</article>
<div class="view-all abs">VIEW ALL EVENTS</div>

<!-- sidebar: login -->
<aside class="panel abs" style="left:555px;top:207px;width:159px;height:156px">
  <div class="panel-title abs" style="left:9px;top:9px">MEMBER LOG IN</div>
  <div class="field abs" style="left:9px;top:31px;width:140px">USERNAME</div>
  <div class="field abs" style="left:9px;top:57px;width:140px">PASSWORD</div>
  <div class="check abs" style="left:10px;top:87px"></div>
  <div class="panel-link abs" style="left:23px;top:86px">Keep me logged in</div>
  <div class="btn btn-navy abs" style="left:104px;top:82px;width:45px;height:18px">LOG IN</div>
  <div class="panel-link abs" style="left:11px;top:112px">Forgotten login?</div>
  <div class="panel-link abs" style="left:11px;top:127px">Not a MentraLoop yet?</div>
</aside>

<!-- sidebar: quick sign up -->
<aside class="panel abs" style="left:555px;top:373px;width:159px;height:297px">
  <div class="panel-title abs" style="left:9px;top:10px">QUICK SIGN UP</div>
  <ul class="perk-list abs" style="left:9px;top:31px;width:145px">
    <li><svg class="tick" viewBox="0 0 10 10"><path d="M1 5l3 3 5-7" fill="none" stroke="#2c4f86" stroke-width="2"/></svg><span>Free to join</span></li>
    <li><svg class="tick" viewBox="0 0 10 10"><path d="M1 5l3 3 5-7" fill="none" stroke="#2c4f86" stroke-width="2"/></svg><span>3 issues of Coaching<br>Research in Practice</span></li>
    <li><svg class="tick" viewBox="0 0 10 10"><path d="M1 5l3 3 5-7" fill="none" stroke="#2c4f86" stroke-width="2"/></svg><span>Monthly issues of Lessons<br>from the Field</span></li>
    <li><svg class="tick" viewBox="0 0 10 10"><path d="M1 5l3 3 5-7" fill="none" stroke="#2c4f86" stroke-width="2"/></svg><span>Access to our community</span></li>
    <li><svg class="tick" viewBox="0 0 10 10"><path d="M1 5l3 3 5-7" fill="none" stroke="#2c4f86" stroke-width="2"/></svg><span>Online profile</span></li>
  </ul>
  <div class="field abs" style="left:9px;top:155px;width:140px">FIRST NAME</div>
  <div class="field abs" style="left:9px;top:182px;width:140px">LAST NAME</div>
  <div class="field abs" style="left:9px;top:209px;width:140px">EMAIL ADDRESS</div>
  <div class="check abs" style="left:10px;top:237px"></div>
  <div class="panel-link abs" style="left:24px;top:235px;line-height:13px">I have read the MentraLoop<br>terms and conditions.</div>
  <div class="btn btn-navy abs" style="left:72px;top:270px;width:77px;height:19px">SIGN UP NOW</div>
</aside>

<!-- promo -->
<div class="promo abs" role="img" aria-label="Business people seated in chairs on a beach under a blue sky"></div>
<div class="promo-title abs">Focusing on Change</div>
<ul class="promo-list abs"><li>• Changing Behavior</li><li>• Driving Results</li><li>• Creating Sustainable Growth</li></ul>

<div class="h-rule abs" style="left:80px;top:798px;width:634px"></div>

<!-- welcome -->
<h2 class="section-title abs" style="left:80px;top:811px">Welcome to Our MainPage</h2>
<div class="title-rule abs" style="left:80px;top:835px;width:254px"></div>
<div class="welcome-copy abs">
  <p>MentraLoop is an international community of coaches who engage in reciprocal coaching, mentoring and supervision for their own personal and professional development.</p>
  <p>By giving coaching and mentoring, MentraLoops receive coaching and mentoring, and by participating in supervision, MentraLoops give and receive through collaborative learning.</p>
  <p>Therefore, as a MentraLoop, you pay for your coaching, mentoring and supervision by giving it to another coach. As a result, because you're only paying us to orchestrate the reciprocal process, not for the coaching/mentoring/supervision itself, 8 sessions can cost much less than you'd normally pay for one session!</p>
</div>

<!-- testimonials -->
<h2 class="section-title abs" style="left:508px;top:811px">Testimonials</h2>
<div class="title-rule abs" style="left:508px;top:835px;width:206px"></div>
<div class="quote-box abs"></div>
<div class="quote-mark abs" style="left:514px;top:848px">“</div>
<p class="quote-text abs">I would urge all new coaches to take advantage of Mentraloop and use the tools given to gain more experience and the priceless opportunities to give back is well worth the rewards. Besides learning and growing within the community the best that I have received from being a member of Mentraloop is meeting new people....</p>
<div class="quote-mark abs" style="left:614px;top:954px">”</div>
<div class="quote-name abs">Dana Whitfield</div>
<div class="quote-place abs">United States, 2013</div>
<div class="quote-photo abs" role="img" aria-label="Portrait of the member giving the testimonial"></div>

<!-- supporters -->
<section class="supporters abs"></section>
<h2 class="section-title abs" style="left:80px;top:1038px">Thanks to our Supporters</h2>
<svg class="arrow abs" style="left:686px" width="10" height="14" viewBox="0 0 10 14"><path d="M8 1L2 7l6 6" fill="none" stroke="#444" stroke-width="2"/></svg>
<svg class="arrow abs" style="left:706px" width="10" height="14" viewBox="0 0 10 14"><path d="M2 1l6 6-6 6" fill="none" stroke="#444" stroke-width="2"/></svg>
<div class="supporter abs" style="left:80px">Bravion.co</div>
<div class="supporter abs" style="left:209px">Talvero</div>
<div class="supporter abs" style="left:338px">Nimbrel's</div>
<div class="supporter abs" style="left:466px">Orbanta</div>
<div class="supporter abs" style="left:595px">Castellan.Co</div>

<!-- footer -->
<footer class="site-footer abs"></footer>
<div class="copyright abs">Copyright © 2009-2013 <span>MentraLoop Pty Ltd.</span><br>All Right Reserved</div>
<div class="connect abs">Connect with our Community</div>
<div class="social abs" style="left:596px;background:#3b5b9a" role="img" aria-label="Social network link"></div>
<div class="social abs" style="left:622px;background:#4bb3e0" role="img" aria-label="Social network link"></div>
<div class="social abs" style="left:649px;background:#2f76b0" role="img" aria-label="Social network link"></div>

</body>
</html>
```